Business Card Design for a coaching and consulting company (usage of existing logo)

We need a business card design for a new business start up (coaching & consulting) incorporating an existing logo that has just been created by a brandhollow designer.

The business card should pick up the existing logo and its colours (please check out variations as well) and look fresh, light, open and professional. The business card must be applicable for worldwide clients and must adhere to the standard Australian business card measurements. We are open for fun designs that require special print techniques as long as it doesn't get too expensive/fancy in the print process. We prefer versions that use both sides of the business card as we personally find 1-siders a little bit boring.

```html
<!DOCTYPE html>
<html lang="en">
<head>
<meta charset="utf-8">
<title>Beaconpoint Business Card</title>
<link rel="stylesheet" href="https://fonts.googleapis.com/css2?family=Open+Sans:wght@400;600;700&display=swap">
<style>
  :root {
    --stage: #e9e6e2;
    --card: #050505;
    --white: #ffffff;
    --muted: #d8d8d8;
    --gold: #f4b82a;
    --slate: #4a4a4a;
    --art-top: #3b3a33;
    --art-bottom: #b8472a;
  }
  * { box-sizing: border-box; margin: 0; padding: 0; }
  html, body { width: 1200px; height: 463px; overflow: hidden; }
  body {
    background: var(--stage);
    font-family: "Open Sans", Arial, sans-serif;
    color: var(--white);
    position: relative;
  }
  .card {
    position: absolute;
    top: 76px;
    width: 545px;
    height: 311px;
    background: var(--card);
    border-radius: 4px;
    overflow: hidden;
  }
  .card--front { left: 35px; }
  .card--back { left: 620px; }

  /* front side */
  .edge-accent { position: absolute; left: 0; width: 9px; }
  .edge-accent--gold { top: 24px; height: 140px; background: var(--gold); border-radius: 0 4px 4px 0; }
  .edge-accent--slate { top: 172px; height: 130px; background: var(--slate); border-radius: 0 4px 4px 0; }

  .brand {
    position: absolute;
    display: flex;
    align-items: center;
    gap: 10px;
  }
  .brand__dot { width: 16px; height: 16px; border-radius: 50%; flex: none; }
  .brand__name { font-weight: 600; font-size: 26px; letter-spacing: -0.5px; line-height: 1; }
  .brand__tagline { font-size: 14px; margin-top: 4px; }

  .card--front .brand { left: 38px; top: 48px; }
  .card--front .brand__dot { background: var(--gold); }
  .card--front .brand__tagline { color: var(--gold); }

  .contact {
    position: absolute;
    left: 292px;
    top: 96px;
    padding-left: 12px;
    border-left: 2px solid var(--white);
    height: 200px;
  }
  .contact__name { font-weight: 700; font-size: 17px; letter-spacing: 0.2px; }
  .contact__role { font-size: 15px; margin-top: 2px; color: var(--muted); }
  .contact__list { list-style: none; margin-top: 18px; font-size: 14px; line-height: 21px; }
  .contact__list li { display: flex; align-items: center; gap: 5px; }
  .contact__list svg { width: 12px; height: 12px; fill: var(--white); flex: none; }
  .contact__address { font-size: 14px; line-height: 21px; margin-top: 18px; font-style: normal; }

  /* back side */
  .feature-art {
    position: absolute;
    left: 30px;
    top: 40px;
    width: 250px;
    height: 262px;
    background: linear-gradient(180deg, var(--art-top), var(--art-bottom));
    border-radius: 4px;
  }
  .card--back .brand { left: 300px; top: 92px; }
  .card--back .brand__dot { border: 2px solid var(--white); }
  .back-url {
    position: absolute;
    left: 326px;
    top: 172px;
    font-size: 9px;
    letter-spacing: 1.4px;
  }
</style>
</head>
<body>
  <section class="card card--front">
    <span class="edge-accent edge-accent--gold"></span>
    <span class="edge-accent edge-accent--slate"></span>

    <div class="brand">
      <span class="brand__dot"></span>
      <div>
        <div class="brand__name">Beaconpoint</div>
        <div class="brand__tagline">Coaching &amp; Consulting</div>
      </div>
    </div>

    <div class="contact">
      <p class="contact__name">Marla Venholt</p>
      <p class="contact__role">Owner</p>
      <ul class="contact__list">
        <li>
          <svg viewBox="0 0 12 12" aria-hidden="true"><circle cx="6" cy="6" r="6"/><path d="M3.6 3c.6-.4 1 .1 1.3.8.2.5-.4.8-.3 1.2.3.8 1 1.5 1.7 1.8.4.1.7-.5 1.2-.3.7.3 1.2.7.8 1.3-.5.8-1.4.9-2.3.5C4.6 7.7 3.9 6.6 3.3 5c-.3-.8-.2-1.5.3-2z" fill="#050505"/></svg>
          555-010-2468
        </li>
        <li>
          <svg viewBox="0 0 12 12" aria-hidden="true"><circle cx="6" cy="6" r="6"/><path d="M2.8 4h6.4v4.2H2.8z" fill="#050505"/><path d="M2.8 4 6 6.4 9.2 4" stroke="#fff" stroke-width="0.8" fill="none"/></svg>
          marlav@beaconpoint.com
        </li>
        <li>
          <svg viewBox="0 0 12 12" aria-hidden="true"><circle cx="6" cy="6" r="6"/><g stroke="#050505" stroke-width="0.9" fill="none"><ellipse cx="6" cy="6" rx="2.2" ry="4.6"/><path d="M1.4 6h9.2M2.2 3.6h7.6M2.2 8.4h7.6"/></g></svg>
          www.beaconpoint.com
        </li>
      </ul>
      <address class="contact__address">Street Name, City Name<br>State Zipcode</address>
    </div>
  </section>

  <section class="card card--back">
    <div class="feature-art" role="img" aria-label="Illustration of a red and white striped lighthouse casting light beams"></div>

    <div class="brand">
      <span class="brand__dot"></span>
      <div>
        <div class="brand__name">Beaconpoint</div>
        <div class="brand__tagline">Coaching &amp; Consulting</div>
      </div>
    </div>
    <p class="back-url">www.beaconpoint.com</p>
  </section>
</body>
</html>
```